Profesional personal website needs design and business card

I need a business card with my professional name as a logo "Marlo Vitality" for my business. I am a Wellness Coach, consultant and trainer. So it should be professional, wellness oriented and modern.

Target Market(s)

Private clients, governments, corporations. Luxury and high market.

Industry/Entity Type

Health And Wellness

Contact Information for Business Card

Marlo Vitality should be the logo

Colors

Designer to choose colors to be used in the design.

Requirements
Must have
• Marlo Vitality
• Name: Tomás Arribal
• Wellness Coach, Consultant & Trainer.
• Website: www.marlovitality.example
• Phone:
• Spain (+34) 612 480 397
• (USA) +1 (555) 318 2046
Nice to have
• The most important is the design of "Marlo Vitality", as this is going to be my personal brand logo. It should be professional, wellness, high end and actual.
Should not have
• no golds, no baroque style..

```html
<!DOCTYPE html>
<html lang="en">
<head>
<meta charset="UTF-8">
<title>Marlo Vitality — Business Card</title>
<link href="https://fonts.googleapis.com/css2?family=Montserrat:wght@400;500;700;800&display=swap" rel="stylesheet">
<style>
  :root{
    --bg:#1a1a1a;
    --card:#2a2a2a;
    --brand-blue:#0f22b4;
    --accent:#f7c500;
    --ink:#ffffff;
  }
  *{margin:0;padding:0;box-sizing:border-box}
  html,body{width:1200px;height:900px;overflow:hidden}
  body{
    background:var(--bg);
    font-family:'Montserrat',sans-serif;
    position:relative;
  }
  .card{
    position:absolute;
    left:250px;
    width:700px;
    height:400px;
    background:var(--card);
    border-bottom:7px solid var(--accent);
  }
  .card--front{top:30px}
  .card--back{top:465px}

  .brand-name{
    font-family:'Montserrat',sans-serif;
    font-weight:800;
    color:var(--brand-blue);
    text-transform:uppercase;
    letter-spacing:1px;
    white-space:nowrap;
  }
  .card--front .brand-name{
    position:absolute;
    top:50%;left:50%;
    transform:translate(-50%,-50%);
    font-size:58px;
  }
  .card--back .brand-name{
    position:absolute;
    left:40px;top:172px;
    font-size:30px;
  }
  .divider{
    position:absolute;
    left:340px;top:95px;
    width:3px;height:200px;
    background:var(--accent);
  }
  .contact{
    position:absolute;
    left:375px;top:100px;
    width:300px;
    color:var(--ink);
  }
  .contact__name{
    color:var(--accent);
    font-weight:700;
    font-size:26px;
    letter-spacing:1px;
    text-transform:uppercase;
    white-space:nowrap;
  }
  .contact__role{
    font-size:17px;
    line-height:1.3;
    margin:4px 0 14px;
  }
  .contact__list{list-style:none}
  .contact__item{
    display:grid;
    grid-template-columns:16px 1fr 26px;
    align-items:center;
    column-gap:10px;
    font-size:18px;line-height:1.5;
    white-space:nowrap;
  }
  .contact__item svg{width:16px;height:16px}
  .contact__item .flag{width:26px;height:17px}
  .contact__web{color:var(--accent)}
</style>
</head>
<body>
  <section class="card card--front">
    <div class="brand-name">Marlo Vitality</div>
  </section>

  <section class="card card--back">
    <div class="brand-name">Marlo Vitality</div>
    <div class="divider"></div>
    <div class="contact">
      <div class="contact__name">Tomás Arribal</div>
      <div class="contact__role">Wellness Coach,<br>Consultant &amp; Trainer</div>
      <ul class="contact__list">
        <li class="contact__item">
          <svg viewBox="0 0 16 16"><path d="M4 1l3 3-2 2c1 2 3 4 5 5l2-2 3 3-2 2C7 14 2 9 2 3z" fill="none" stroke="#f7c500" stroke-width="1.4"/></svg>
          <span>(+34) 612 480 397</span>
          <svg class="flag" viewBox="0 0 26 17" role="img" aria-label="Spain flag">
            <rect width="26" height="17" fill="#c60b1e"/><rect y="4.25" width="26" height="8.5" fill="#f7c500"/>
          </svg>
        </li>
        <li class="contact__item">
          <svg viewBox="0 0 16 16"><rect x="4" y="1" width="8" height="14" rx="1.5" fill="none" stroke="#f7c500" stroke-width="1.4"/><line x1="7" y1="12.5" x2="9" y2="12.5" stroke="#f7c500" stroke-width="1.4"/></svg>
          <span>+1 (555) 318 2046</span>
          <svg class="flag" viewBox="0 0 26 17" role="img" aria-label="United States flag">
            <rect width="26" height="17" fill="#ffffff"/>
            <rect y="0" width="26" height="2.4" fill="#b22234"/><rect y="4.8" width="26" height="2.4" fill="#b22234"/>
            <rect y="9.6" width="26" height="2.4" fill="#b22234"/><rect y="14.4" width="26" height="2.6" fill="#b22234"/>
            <rect width="11" height="9" fill="#3c3b6e"/>
          </svg>
        </li>
        <li class="contact__item">
          <svg viewBox="0 0 16 16"><rect x="1" y="3.5" width="14" height="9" fill="none" stroke="#f7c500" stroke-width="1.4"/><path d="M1 3.5l7 5 7-5" fill="none" stroke="#f7c500" stroke-width="1.4"/></svg>
          <span style="grid-column:2 / 4">info@marlovitality.example</span>
        </li>
        <li class="contact__item">
          <svg viewBox="0 0 16 16"><circle cx="8" cy="8" r="6.5" fill="none" stroke="#f7c500" stroke-width="1.3"/><ellipse cx="8" cy="8" rx="3" ry="6.5" fill="none" stroke="#f7c500" stroke-width="1.1"/><line x1="1.5" y1="8" x2="14.5" y2="8" stroke="#f7c500" stroke-width="1.1"/></svg>
          <span style="grid-column:2 / 4">www.<span class="contact__web">marlovitality</span>.example</span>
        </li>
      </ul>
    </div>
  </section>
</body>
</html>
```